Private Security Company Business Card and Logo Design

Looking for a modern conservative business card design for our new private security company Harbor Ridge Guard Co., Inc. or HRGC for short.
Private Security Services. The current logo we have is not very good and honestly would like a sharp logo for the card instead of using the one we have now. Open to ideas. I am easy just looking for something nicer then what I can personally design on cardmillo. I searched on zintoo for Security Company business cards went to images and found some nice designs that were made here.

Target Market(s)

Security Services

Industry/Entity Type

Business

Contact Information for Business Card

Harbor Ridge Guard Co., Inc.
President, cell,office,fax,email, website,
Logo etc, whatever is needed for a standard business card
Can provide personal Information later.

Colors
0556a4
ffffff
474747

Requirements
Must have
• Modern but conservative,
Nice to have
• color choices
• Blue, white, Grey

```html
<!DOCTYPE html>
<html lang="en">
<head>
<meta charset="utf-8">
<title>Harbor Ridge Guard Co., Inc. — Business Card</title>
<link rel="stylesheet" href="https://fonts.googleapis.com/css2?family=Oswald:wght@500&family=Roboto:wght@400&display=swap">
<style>
  :root {
    --brand-blue: #0556a4;
    --accent-blue: #2a63d8;
    --white: #ffffff;
    --silver: #c9ccd1;
    --grey: #474747;
    --stage-top: #d4d4d4;
    --stage-bottom: #6e6e6e;
    --card-top: #1b1d20;
    --card-bottom: #0b0c0d;
  }
  * { margin: 0; padding: 0; box-sizing: border-box; }
  html, body { width: 1200px; height: 900px; overflow: hidden; }
  body {
    background: linear-gradient(180deg, var(--stage-top) 0%, #a9a9a9 45%, var(--stage-bottom) 100%);
    position: relative;
    font-family: "Roboto", Arial, sans-serif;
  }
  .card {
    position: absolute;
    top: 300px;
    width: 525px;
    height: 300px;
    border-radius: 24px;
    background: linear-gradient(180deg, var(--card-top) 0%, var(--card-bottom) 100%);
    box-shadow: 0 18px 30px rgba(0,0,0,0.35);
    overflow: hidden;
  }
  .card--front { left: 50px; }
  .card--back { left: 625px; }

  .emblem {
    position: absolute;
    left: 50%;
    transform: translateX(-50%);
    width: 64px;
    height: 64px;
    border-radius: 50%;
    background: var(--brand-blue);
    border: 3px solid var(--silver);
  }
  .card--front .emblem { top: 82px; }
  .card--back .emblem { top: 34px; }

  .wordmark {
    position: absolute;
    left: 0; right: 0;
    text-align: center;
    font-family: "Oswald", "Arial Narrow", sans-serif;
    font-weight: 500;
    font-size: 22px;
    letter-spacing: 0.5px;
    color: var(--silver);
    text-transform: uppercase;
  }
  .card--front .wordmark { top: 166px; }
  .card--back .wordmark { top: 112px; font-size: 20px; }

  .divider {
    position: absolute;
    left: 0; right: 0;
    top: 170px;
    height: 2px;
    background: linear-gradient(90deg, #5a5d62 0%, #e8e9eb 70%, #8d9096 100%);
  }

  .holder {
    position: absolute;
    top: 200px;
    right: 258px;
    text-align: right;
  }
  .holder__name {
    color: var(--accent-blue);
    font-size: 17px;
    line-height: 20px;
  }
  .holder__title {
    color: var(--white);
    font-size: 11px;
    margin-top: 2px;
  }

  .contact {
    position: absolute;
    top: 190px;
    left: 282px;
    padding-left: 8px;
    border-left: 1px solid var(--silver);
    list-style: none;
  }
  .contact__item {
    display: flex;
    align-items: center;
    gap: 5px;
    color: var(--white);
    font-size: 11.5px;
    line-height: 16px;
    white-space: nowrap;
  }
  .contact__icon { width: 11px; height: 11px; flex: none; fill: var(--accent-blue); }
</style>
</head>
<body>

  <section class="card card--front" aria-label="Card front">
    <div class="emblem"></div>
    <div class="wordmark">Harbor Ridge Guard Co., Inc.</div>
  </section>

  <section class="card card--back" aria-label="Card back">
    <div class="emblem"></div>
    <div class="wordmark">Harbor Ridge Guard Co., Inc.</div>
    <div class="divider"></div>

    <div class="holder">
      <div class="holder__name">Dalton Reyes</div>
      <div class="holder__title">President</div>
    </div>

    <ul class="contact">
      <li class="contact__item">
        <svg class="contact__icon" viewBox="0 0 12 12"><rect x="3" y="0.5" width="6" height="11" rx="1"/><rect x="4" y="2" width="4" height="7" fill="#111"/></svg>
        555 0142 736
      </li>
      <li class="contact__item">
        <svg class="contact__icon" viewBox="0 0 12 12"><path d="M2.5 0.8 4.6 3 3.6 4.6c.7 1.6 2 2.9 3.7 3.7L8.9 7.3 11.2 9.4 10 11.2C5.2 11 1 6.8 .8 2z"/></svg>
        555 0198 411
      </li>
      <li class="contact__item">
        <svg class="contact__icon" viewBox="0 0 12 12"><rect x="0.5" y="2" width="11" height="8" rx="1"/><path d="M1 2.6 6 6.6 11 2.6" stroke="#111" stroke-width="1" fill="none"/></svg>
        dalton@harborridgeguard.com
      </li>
      <li class="contact__item">
        <svg class="contact__icon" viewBox="0 0 12 12"><circle cx="6" cy="6" r="5.5"/><path d="M0.5 6h11M6 .5v11M2 3h8M2 9h8" stroke="#111" stroke-width="0.8" fill="none"/></svg>
        www.harborridgeguard.com
      </li>
      <li class="contact__item">
        <svg class="contact__icon" viewBox="0 0 12 12"><path d="M6 .8 11.5 6H10v5H7.3V8H4.7v3H2V6H.5z"/></svg>
        18 Larkfield Lane, R D 4, Westvale 0417
      </li>
    </ul>
  </section>

</body>
</html>
```